Anzeigengestaltung für Zahnarztpraxis
Zielgruppe
Zahnarztpraxis
Aufgabenstellung
Möchte eine moderne Stellenanzeige, ggf. einen zum Logo farblich passenden Rahmen; ggf. noch mit Bildern

```html
<!DOCTYPE html>
<html lang="de">
<head>
<meta charset="utf-8">
<title>Stellenanzeige Zahnarztpraxis Lindenau</title>
<link href="https://fonts.googleapis.com/css2?family=Poppins:wght@400;500;600;700&display=swap" rel="stylesheet">
<style>
  :root {
    --navy: #3b5380;
    --green: #9bc04a;
    --ink: #3d3d45;
    --paper: #f2f2f3;
    --panel: #e4e5e9;
    --rule: #8a8a8f;
  }
  * { box-sizing: border-box; margin: 0; padding: 0; }
  html, body { width: 1200px; height: 1103px; overflow: hidden; background: #d9d9da; }
  body { font-family: "Poppins", sans-serif; color: var(--ink); }
  .ad {
    position: absolute; left: 14px; top: 14px; width: 1172px; height: 1075px;
    background: var(--paper); border: 1px solid var(--rule); overflow: hidden;
  }
  .header-band {
    position: absolute; left: 0; top: 0; width: 735px; height: 205px; background: var(--navy);
  }
  .brand {
    position: absolute; left: 100px; top: 72px; display: flex; align-items: center; gap: 18px;
    color: #fff; font-weight: 500; font-size: 34px; line-height: 1.05;
  }
  .brand-dot { width: 62px; height: 62px; border-radius: 50%; border: 7px solid #fff; }
  .callout-block {
    position: absolute; left: 735px; top: 0; width: 437px; height: 225px; background: var(--green);
    display: flex; align-items: center; justify-content: center; text-align: center;
    color: var(--navy); font-weight: 700; font-size: 30px; line-height: 1.25; letter-spacing: 1px;
  }
  .callout-block .white { color: #fff; }
  .kicker {
    position: absolute; left: 70px; top: 250px; color: var(--green); font-weight: 600;
    font-size: 25px; letter-spacing: 1px;
  }
  .job-titles {
    position: absolute; left: 66px; top: 292px; color: var(--navy); font-weight: 600;
    font-size: 40px; line-height: 1.25;
  }
  .section-head { color: var(--navy); font-weight: 700; font-size: 25px; letter-spacing: .5px; margin-bottom: 18px; }
  .column { position: absolute; z-index: 2; }
  .benefits { left: 66px; top: 418px; width: 470px; }
  .requirements { left: 590px; top: 498px; width: 540px; }
  .checklist { list-style: none; font-size: 22.5px; line-height: 1.3; }
  .checklist li { position: relative; padding-left: 46px; }
  .checklist li svg { position: absolute; left: 2px; top: 4px; width: 22px; height: 16px; }
  .closing { margin-top: 20px; color: var(--navy); font-weight: 600; font-size: 22px; line-height: 1.3; }
  .apply-panel {
    position: absolute; left: 0; bottom: 0; width: 100%; height: 195px; background: var(--panel);
    padding: 32px 0 0 56px; z-index: 1;
  }
  .apply-panel p { font-size: 22.5px; line-height: 1.35; max-width: 720px; }
  .apply-panel .lead { color: var(--navy); font-weight: 700; font-size: 34px; }
  .sep { color: var(--green); }
  .apply-badge {
    position: absolute; right: 110px; bottom: 22px; width: 200px; height: 200px; border-radius: 50%;
    background: var(--navy); color: #fff; font-weight: 700; font-size: 27px; line-height: 1.15;
    display: flex; align-items: center; justify-content: center; text-align: center; letter-spacing: 1px;
    z-index: 3;
  }
  .apply-badge .accent { color: var(--green); }
</style>
</head>
<body>
<main class="ad">
  <div class="header-band">
    <div class="brand"><span class="brand-dot"></span><span>Zahnarztpraxis<br>Lindenau</span></div>
  </div>
  <div class="callout-block"><p><span class="white">VERSTÄRKUNG</span><br>GESUCHT!</p></div>

  <p class="kicker">WIR SUCHEN IN VOLLZEIT:</p>
  <h1 class="job-titles">Zahnmedizinische Fachangestellte (m,w,d)<br>Zahnmedizinische Prophylaxeassistentin (m,w,d)</h1>

  <section class="column benefits">
    <h2 class="section-head">DEINE VORTEILE:</h2>
    <ul class="checklist">
      <li><svg viewBox="0 0 22 16"><path d="M2 8l6 6L20 2" fill="none" stroke="#9bc04a" stroke-width="3"/></svg>Geregelte Arbeitszeiten</li>
      <li><svg viewBox="0 0 22 16"><path d="M2 8l6 6L20 2" fill="none" stroke="#9bc04a" stroke-width="3"/></svg>Top moderne Ausstattung</li>
      <li><svg viewBox="0 0 22 16"><path d="M2 8l6 6L20 2" fill="none" stroke="#9bc04a" stroke-width="3"/></svg>Spannende Mitarbeiterevents</li>
      <li><svg viewBox="0 0 22 16"><path d="M2 8l6 6L20 2" fill="none" stroke="#9bc04a" stroke-width="3"/></svg>Etabliertes Qualitätsmanage-<br>ment und klare Strukturen</li>
      <li><svg viewBox="0 0 22 16"><path d="M2 8l6 6L20 2" fill="none" stroke="#9bc04a" stroke-width="3"/></svg>Flexible Urlaubsplanung</li>
      <li><svg viewBox="0 0 22 16"><path d="M2 8l6 6L20 2" fill="none" stroke="#9bc04a" stroke-width="3"/></svg>Sehr gute Gehalts- und<br>Weiterbildungsmöglichkeiten</li>
      <li><svg viewBox="0 0 22 16"><path d="M2 8l6 6L20 2" fill="none" stroke="#9bc04a" stroke-width="3"/></svg>Kostenfreie Zahnbehandlungen<br>inkl. Bleaching</li>
    </ul>
  </section>

  <section class="column requirements">
    <h2 class="section-head">WAS UNS WICHTIG IST:</h2>
    <ul class="checklist">
      <li><svg viewBox="0 0 22 16"><path d="M2 8l6 6L20 2" fill="none" stroke="#9bc04a" stroke-width="3"/></svg>Du bist aufgeschlossen<br>und motiviert</li>
      <li><svg viewBox="0 0 22 16"><path d="M2 8l6 6L20 2" fill="none" stroke="#9bc04a" stroke-width="3"/></svg>Du bist kommunikativ und<br>kontaktfreudig im Umgang<br>mit Menschen</li>
      <li><svg viewBox="0 0 22 16"><path d="M2 8l6 6L20 2" fill="none" stroke="#9bc04a" stroke-width="3"/></svg>Du hast Freude an deiner Arbeit</li>
    </ul>
    <p class="closing">Dann bist DU die Verstärkung,<br>die wir suchen!</p>
  </section>

  <section class="apply-panel">
    <p><span class="lead">Interesse?</span> Wir freuen uns über eine schriftliche Bewerbung per Post an: Dr. Harbeck <span class="sep">|</span> Gartenstr. 12 <span class="sep">|</span> 73400 Lindenau oder per Mail an: timo-harbeck@mailpost.de</p>
  </section>
  <div class="apply-badge"><p>BEWIRB<br>DICH<br><span class="accent">JETZT!</span></p></div>
</main>
</body>
</html>
```